Business card design needed

Chasing a very simplistic modern design with a logo incorporating "TRV".
I'm starting a plumbing business.
I do water, sanitary and drainage plumbing that will cover residential, commercial, rental, rural, excavation, new housing and all maintanence requirements.

Industry/Entity Type

Business

Contact Information for Business Card

TRV PLUMBING SERVICES
DEAN HOLLOWBY - LICENSED PLUMBER
PHONE: 0481926574
E-MAIL: hollodt7@wirelane.com
NORTHERN SUBURBS

Requirements
Must have
• lower case email address

```html
<!DOCTYPE html>
<html lang="en">
<head>
<meta charset="utf-8">
<title>TRV Plumbing Services – Business Card</title>
<link rel="stylesheet" href="https://fonts.googleapis.com/css2?family=Exo+2:wght@600;700&family=Open+Sans:wght@400;700&display=swap">
<style>
  :root {
    --backdrop: #2e2e2e;
    --card-dark: #231f20;
    --card-light: #ffffff;
    --teal: #1b9db3;
    --teal-light: #5cc3d4;
    --silver: #e8e8e8;
    --ink: #231f20;
  }
  * { margin: 0; padding: 0; box-sizing: border-box; }
  html, body {
    width: 1200px;
    height: 900px;
    overflow: hidden;
    background: var(--backdrop);
  }
  .card {
    position: absolute;
    left: 100px;
    top: 150px;
    width: 1000px;
    height: 600px;
    background: var(--card-light);
    overflow: hidden;
    font-family: "Open Sans", Arial, sans-serif;
  }
  .card-header {
    position: absolute;
    left: 0; top: 0;
    width: 100%;
    height: 296px;
    background: var(--card-dark);
  }
  .brand-name {
    position: absolute;
    left: 0; top: 38px;
    width: 100%;
    text-align: center;
    font-family: "Exo 2", Arial, sans-serif;
    font-weight: 700;
    font-size: 150px;
    line-height: 1;
    color: var(--teal);
  }
  .brand-tagline {
    position: absolute;
    left: 0; top: 196px;
    width: 100%;
    text-align: center;
    font-family: "Exo 2", Arial, sans-serif;
    font-weight: 600;
    font-size: 66px;
    line-height: 1;
    letter-spacing: 1px;
  }
  .brand-tagline .word-plumbing { color: var(--teal); }
  .brand-tagline .word-services { color: var(--silver); }
  .header-rule {
    position: absolute;
    left: 0; top: 296px;
    width: 100%;
    height: 10px;
    background: linear-gradient(90deg, var(--teal) 0%, var(--teal) 50%, var(--teal-light) 52%, var(--teal) 56%, var(--teal) 100%);
  }
  .contact {
    position: absolute;
    left: 62px;
    top: 338px;
    color: var(--ink);
  }
  .contact-name {
    font-weight: 700;
    font-size: 40px;
    line-height: 1.2;
    color: var(--teal);
  }
  .contact-role {
    font-size: 34px;
    line-height: 1.3;
    margin-bottom: 16px;
  }
  .contact-area {
    font-weight: 700;
    font-size: 27px;
    line-height: 1.35;
    margin-left: 6px;
  }
  .contact-line {
    font-size: 27px;
    line-height: 1.35;
    margin-left: 6px;
  }
  .contact-label { color: var(--teal); }
  .brand-watermark {
    position: absolute;
    right: -20px;
    bottom: -46px;
    font-family: "Exo 2", Arial, sans-serif;
    font-weight: 700;
    font-size: 230px;
    line-height: 1;
    color: var(--teal);
  }
</style>
</head>
<body>
  <main class="card">
    <header class="card-header">
      <div class="brand-name">TRV</div>
      <div class="brand-tagline"><span class="word-plumbing">PLUMBING</span> <span class="word-services">SERVICES</span></div>
    </header>
    <div class="header-rule"></div>
    <section class="contact">
      <p class="contact-name">Dean Hollowby</p>
      <p class="contact-role">Licensed Plumber</p>
      <p class="contact-area">Northern Suburbs</p>
      <p class="contact-line"><span class="contact-label">Phone:</span> 0481 926 574</p>
      <p class="contact-line"><span class="contact-label">E-mail:</span> hollodt7@wirelane.com</p>
    </section>
    <div class="brand-watermark" aria-hidden="true">TRV</div>
  </main>
</body>
</html>
```